Business Card + Stationary
TBV Financial Group
Professional
Dale Morrow
Business Development Manager
2718 SW 9th Ave. Suite 1146
Lakemoor, WA 98071 Toll Free
dale@tbvfinancialgroup.example
www.tbvfinancialgroup.example
want to modernize & update website and design.
Feel free to update/ change TBV logo as you see fit.
Logo
More of a high res logo
eps logo
TBV Background (not sure if the quality is good enough though)

```html
<!DOCTYPE html>
<html lang="en">
<head>
<meta charset="utf-8">
<title>TBV Financial Group – Business Cards</title>
<link href="https://fonts.googleapis.com/css2?family=Tinos:wght@400;700&display=swap" rel="stylesheet">
<style>
  :root {
    --navy: #1f4e8c;
    --navy-deep: #173e72;
    --ink: #2a2f3a;
    --grey: #6b7280;
    --paper: #ffffff;
    --backdrop: #eef0f3;
  }
  * { box-sizing: border-box; margin: 0; padding: 0; }
  html, body { width: 1200px; height: 1006px; overflow: hidden; }
  body {
    background: var(--backdrop);
    font-family: "Tinos", "Times New Roman", serif;
    color: var(--ink);
    position: relative;
  }
  .card {
    position: absolute;
    width: 700px;
    height: 400px;
    border-radius: 22px;
    overflow: hidden;
    box-shadow: 0 6px 20px rgba(0,0,0,.12);
  }

  /* Back */
  .card-back {
    left: 250px; top: 70px;
    background: var(--navy);
    color: var(--paper);
  }
  .back-mark {
    position: absolute; left: 0; right: 0; top: 140px;
    display: flex; justify-content: center; align-items: center; gap: 14px;
  }
  .back-mark .square { width: 34px; height: 34px; background: var(--paper); }
  .back-mark .name { font-size: 52px; font-weight: 700; letter-spacing: 2px; }
  .back-web {
    position: absolute; left: 0; right: 0; bottom: 44px;
    text-align: center; font-size: 17px; letter-spacing: 3px;
  }

  /* Front */
  .card-front {
    left: 250px; top: 530px;
    background: var(--paper);
  }
  .front-mark {
    position: absolute; left: 110px; top: 40px;
    display: flex; align-items: center; gap: 14px;
    color: var(--navy);
  }
  .front-mark .square { width: 40px; height: 40px; background: var(--navy); }
  .front-mark .name { font-size: 60px; font-weight: 700; letter-spacing: 2px; line-height: 1; }
  .front-mark .tagline {
    display: block; font-size: 12px; letter-spacing: 2.5px; margin-top: 4px;
    color: var(--ink);
  }
  .contact-list {
    position: absolute; left: 34px; top: 140px;
    list-style: none; font-size: 13px; line-height: 23px; color: var(--ink);
  }
  .contact-list li { display: flex; align-items: center; gap: 9px; }
  .contact-list svg { width: 11px; height: 11px; fill: var(--navy); flex: none; }
  .band { position: absolute; left: 0; bottom: 0; width: 700px; height: 110px; }
  .person {
    position: absolute; right: 40px; top: 262px; text-align: right;
  }
  .person .name { font-size: 18px; font-weight: 700; color: var(--navy); }
  .person .role { font-size: 13px; color: var(--grey); margin-top: 2px; }
  .front-web {
    position: absolute; right: 40px; bottom: 20px;
    font-size: 16px; line-height: 20px; letter-spacing: 2.5px; color: var(--paper);
  }
</style>
</head>
<body>

<section class="card card-back" aria-label="Card back">
  <div class="back-mark"><span class="square"></span><span class="name">TBV</span></div>
  <p class="back-web">www.tbvfinancialgroup.example</p>
</section>

<section class="card card-front" aria-label="Card front">
  <div class="front-mark">
    <span class="square"></span>
    <div><span class="name">TBV</span><span class="tagline">FINANCIAL GROUP INC.</span></div>
  </div>

  <ul class="contact-list">
    <li><svg viewBox="0 0 10 10"><path d="M5 0a3.5 3.5 0 0 0-3.5 3.5C1.5 6 5 10 5 10s3.5-4 3.5-6.5A3.5 3.5 0 0 0 5 0zm0 5a1.5 1.5 0 1 1 0-3 1.5 1.5 0 0 1 0 3z"/></svg>2718 SW 9th Ave. Suite 1146</li>
    <li><svg viewBox="0 0 10 10"><circle cx="5" cy="5" r="3"/></svg>Lakemoor, WA 98071 Toll Free</li>
    <li><svg viewBox="0 0 10 10"><path d="M2 0h2l1 3-1.5 1a6 6 0 0 0 2.5 2.5L7 5l3 1v2c0 1-1 2-2 2A8 8 0 0 1 0 2c0-1 1-2 2-2z"/></svg>Tel 555 010 2279</li>
    <li><svg viewBox="0 0 10 10"><rect x="1" y="2" width="8" height="6"/></svg>Fax 555 010 2280</li>
    <li><svg viewBox="0 0 10 10"><path d="M0 2h10v6H0zM0 2l5 3.5L10 2"/></svg>dale@tbvfinancialgroup.example</li>
    <li><svg viewBox="0 0 10 10"><circle cx="5" cy="5" r="4.5"/></svg>www.tbvfinancialgroup.example</li>
  </ul>

  <svg class="band" viewBox="0 0 700 110" aria-hidden="true">
    <rect x="0" y="14" width="245" height="3" fill="var(--navy-deep)"/>
    <path d="M0 24H250C272 24 278 50 300 50H700V110H0Z" fill="var(--navy)"/>
  </svg>

  <div class="person">
    <p class="name">Dale Morrow</p>
    <p class="role">Business Development Manager</p>
  </div>
  <p class="front-web">www.tbvfinancialgroup.example</p>
</section>

</body>
</html>
```